Harbor Nightclub

Nightclub flyer., digital single sided, for KV and PX. I included samples of some previous flyers we've used. Sample Info:
HARBOR
FRIDAYS
FRI MAY 1 2020
DJ VORTAN (club floor)
DJ RUZO & DJ TAV (residents on the lounge floor)
4217 Marlow Avenue Sacramento
www.harborvenuehall.example for list/VIP inquiries

Target Market(s)

Upscale top 40 crowd but want some cool and artsy like the examples included.

Font styles to use
Sans Serif

Requirements
Must have
• Harbor Logo
Nice to have
• Would be nice if the flyer can be incorporated later with DJ photos (sometimes we will add dj photos to pixagram etc). Would like a big city type of feel.
Should not have
• Nothing too sexual.

```html
<!DOCTYPE html>
<html lang="en">
<head>
<meta charset="utf-8">
<title>Harbor Nightclub – Friday Flyer</title>
<link rel="stylesheet" href="https://fonts.googleapis.com/css2?family=Cinzel:wght@400&family=Montserrat:wght@500;700;800&family=Lato:wght@400&display=swap">
<style>
  :root {
    --page-bg: #d9d8d6;
    --sky-pink: #e0467f;
    --sky-magenta: #c02c78;
    --haze-violet: #6a2c9e;
    --night-blue: #2a1f66;
    --floor-dark: #0d0f22;
    --gold: #d9c25a;
    --gold-deep: #b9962e;
    --silver: #d6d6dc;
    --white: #ffffff;
    --date-green: #5fd37a;
    --url-gold: #c9c25c;
  }
  html, body {
    margin: 0;
    width: 1199px;
    height: 1200px;
    overflow: hidden;
    background: var(--page-bg);
  }
  .flyer {
    position: absolute;
    left: 200px;
    top: 30px;
    width: 798px;
    height: 1140px;
    overflow: hidden;
    font-family: "Montserrat", sans-serif;
    color: var(--white);
  }
  .flyer__backdrop {
    position: absolute;
    inset: 0;
    background:
      radial-gradient(ellipse at 80% 10%, rgba(255,120,170,.45), transparent 55%),
      linear-gradient(180deg, var(--sky-pink) 0%, var(--sky-magenta) 25%, var(--haze-violet) 52%, var(--night-blue) 75%, var(--floor-dark) 100%);
  }
  .brand {
    position: absolute;
    left: 0;
    right: 0;
    top: 48px;
    text-align: center;
  }
  .brand__dot {
    width: 96px;
    height: 96px;
    margin: 0 auto;
    border-radius: 50%;
    background: var(--gold);
  }
  .brand__name {
    margin: 34px 0 0;
    font-family: "Cinzel", serif;
    font-weight: 400;
    font-size: 52px;
    letter-spacing: 2px;
    line-height: 1;
    color: var(--white);
  }
  .brand__tagline {
    margin: 10px 0 0;
    font-family: "Lato", sans-serif;
    font-size: 13px;
    letter-spacing: 3px;
    color: rgba(255,255,255,.85);
  }
  .feature {
    position: absolute;
    left: 0;
    top: 0;
    width: 798px;
    height: 1140px;
  }
  .headline {
    position: absolute;
    left: 0;
    right: 0;
    text-align: center;
    margin: 0;
  }
  .headline--main {
    top: 740px;
    font-size: 98px;
    font-weight: 800;
    letter-spacing: -1px;
    line-height: 1;
    background: linear-gradient(90deg, #bcbcc6 0%, #d8d4d0 35%, #c9a85a 65%, #a8782e 100%);
    -webkit-background-clip: text;
    background-clip: text;
    color: transparent;
  }
  .headline--support {
    top: 872px;
    font-size: 43px;
    font-weight: 700;
    color: var(--silver);
  }
  .headline--date {
    top: 940px;
    font-size: 51px;
    font-weight: 800;
    color: var(--date-green);
    letter-spacing: -0.5px;
  }
  .info {
    position: absolute;
    left: 0;
    right: 0;
    text-align: center;
    margin: 0;
    font-family: "Lato", sans-serif;
  }
  .info--address {
    top: 1024px;
    font-size: 22px;
    letter-spacing: 4px;
    color: var(--white);
  }
  .info--web {
    top: 1076px;
    font-size: 20px;
    letter-spacing: 2px;
    color: var(--url-gold);
  }
</style>
</head>
<body>
  <main class="flyer">
    <div class="flyer__backdrop" role="img" aria-label="City skyline at dusk in pink and violet haze above a dancing nightclub crowd with soft light flares"></div>

    <header class="brand">
      <div class="brand__dot"></div>
      <h1 class="brand__name">HARBOR</h1>
      <p class="brand__tagline">NIGHTCLUB + LOUNGE</p>
    </header>

    <svg class="feature" viewBox="0 0 798 1140" aria-hidden="false">
      <defs>
        <linearGradient id="dj-photo-tone" x1="0" y1="0" x2="0" y2="1">
          <stop offset="0" stop-color="#7a3a6e"/>
          <stop offset="0.5" stop-color="#3a2a3c"/>
          <stop offset="1" stop-color="#1c1a24"/>
        </linearGradient>
      </defs>
      <!-- gold accent bars -->
      <polygon points="172,535 210,497 225,512 187,550" fill="var(--gold)"/>
      <polygon points="605,440 670,505 640,535 575,470" fill="var(--gold)" opacity="0.9"/>
      <polygon points="543,725 596,672 611,687 558,740" fill="var(--gold)"/>
      <!-- gold outer frame -->
      <polygon points="383,249 636,502 383,755 130,502" fill="none" stroke="var(--gold)" stroke-width="3"/>
      <!-- artist photo area -->
      <g role="img" aria-label="Photo of the headlining DJ singing into a microphone, headphones around his neck">
        <polygon points="383,270 612,499 383,728 154,499" fill="url(#dj-photo-tone)"/>
        <rect x="255" y="420" width="260" height="310" fill="#1c1a22" opacity="0"/>
      </g>
      <!-- silver inner frame -->
      <polygon points="383,270 612,499 383,728 154,499" fill="none" stroke="var(--silver)" stroke-width="12"/>
    </svg>

    <h2 class="headline headline--main">DJ VORTAN</h2>
    <p class="headline headline--support">DJ RUZO &amp; TAV</p>
    <p class="headline headline--date">FRIDAY | 01 MAY 2020</p>
    <p class="info info--address">4217 MARLOW AVENUE SACRAMENTO</p>
    <p class="info info--web">HARBORVENUEHALL.EXAMPLE FOR LIST/VIP INQUIRIES</p>
  </main>
</body>
</html>
```